Meal Prep website

Website needed for local meal prep service. Simple template to start off with and then looking to be able to take orders from members

Target Market(s)

Toronto area fitness professionals, athletes and people looking for become healthier

Industry/Entity Type

It Service

Number of Pages Required

5+ page

Font styles to use
Sans Serif

Colors
000000

Requirements
Must have
• Landing page giving information about who we are and what type of service we provide.
• Links to social media. Dishvaultfood on Instagram
Nice to have
• E-commerce section allowing users to select and place orders while accepting payments

```html
<!DOCTYPE html>
<html lang="en">
<head>
<meta charset="utf-8">
<title>Dishvault – Meal Prep</title>
<link rel="stylesheet" href="https://fonts.googleapis.com/css2?family=Montserrat:wght@600;700&family=Oswald:wght@400;500&family=Open+Sans:wght@400;600;700&family=Courgette&display=swap">
<style>
:root{
  --green:#2f7a36;
  --green-light:#4caf50;
  --ink:#1d1d1d;
  --text:#555;
  --muted:#999;
  --line:#e3e3e3;
  --grey-bg:#f2f2f2;
  --dark:#232323;
  --darker:#1b1b1b;
  --white:#fff;
}
*{box-sizing:border-box;margin:0;padding:0}
html,body{width:1200px;height:4534px;overflow:hidden}
body{font-family:'Open Sans',sans-serif;color:var(--text);background:var(--white);position:relative}
section,header,footer{position:relative;width:1200px}
.abs{position:absolute}
.title{font-family:'Montserrat',sans-serif;font-weight:700;font-size:33px;color:var(--ink);text-align:center;letter-spacing:1px}
.sub{font-family:'Courgette',cursive;font-size:16px;color:var(--green);text-align:center}

/* top bar */
.topbar{height:27px;background:var(--green);color:#fff;font-size:12px;display:flex;align-items:center;padding-left:160px;gap:28px}
.topbar .social{position:absolute;right:150px;top:0;display:flex}
.topbar .social span{width:27px;height:27px;border-left:1px solid rgba(255,255,255,.3);display:flex;align-items:center;justify-content:center}
.topbar .social i{width:9px;height:9px;background:#fff;display:block}

/* header */
.site-header{height:82px;background:#fff;box-shadow:0 1px 4px rgba(0,0,0,.08);z-index:2}
.brand{left:150px;top:20px;display:flex;align-items:center;gap:10px;font-family:'Montserrat',sans-serif;font-weight:700;font-size:32px;color:var(--green)}
.brand b{width:14px;height:14px;background:var(--green);border-radius:50%}
.nav{left:420px;top:0;height:82px;display:flex;align-items:center;gap:34px;font-family:'Montserrat',sans-serif;font-size:11px;font-weight:600;color:#333}
.nav a{color:inherit;text-decoration:none}
.nav .active{color:var(--green)}
.order-btn{left:916px;top:18px;width:133px;height:48px;background:var(--green);color:#fff;font-family:'Montserrat',sans-serif;font-size:11px;font-weight:700;display:flex;align-items:center;justify-content:center;gap:8px}

/* hero */
.hero{height:520px;background:linear-gradient(135deg,#2a2420,#4a3c30 45%,#6e5a44 70%,#3a302a)}
.hero-title{top:165px;width:100%;text-align:center;font-family:'Montserrat',sans-serif;font-weight:700;font-size:44px;color:#fff}
.hero-call{top:240px;width:100%;text-align:center;font-family:'Montserrat',sans-serif;font-size:34px;font-weight:600;color:#fff}
.hero-call em{font-style:normal;color:var(--green-light)}

/* how to order */
.how{height:477px}
.how .title{position:absolute;top:85px;width:100%}
.how .sub{position:absolute;top:125px;width:100%}
.step{width:220px;text-align:center;top:200px}
.step svg{display:block;margin:0 auto}
.step .num{width:26px;height:26px;border-radius:50%;background:var(--green);color:#fff;font-size:13px;font-weight:700;margin:20px auto 0;display:flex;align-items:center;justify-content:center}
.step p{font-family:'Montserrat',sans-serif;font-weight:600;font-size:17px;color:var(--ink);margin-top:16px;line-height:1.35}

/* menu */
.menu{height:995px;background:var(--grey-bg)}
.menu .title{position:absolute;top:75px;width:100%}
.menu .sub{position:absolute;top:115px;width:100%}
.tabs{top:179px;left:272px;display:flex;gap:12px}
.tabs span{width:118px;height:36px;border:1px solid #ccc;background:#fff;font-size:10px;font-weight:600;color:#555;display:flex;align-items:center;justify-content:center;letter-spacing:.5px}
.tabs .on{background:var(--green);border-color:var(--green);color:#fff}
.dish-card{width:247px;height:305px;background:#fff;text-align:center}
.dish-card .photo{height:224px}
.dish-card .price{font-family:'Oswald',sans-serif;font-size:17px;color:var(--green-light);margin-top:20px}
.dish-card .name{font-family:'Oswald',sans-serif;font-size:14px;color:var(--ink);margin-top:6px}
.ph-toast{background:linear-gradient(135deg,#8a3b20,#c9853f 50%,#6b2a22)}
.ph-chicken{background:linear-gradient(135deg,#7aa84a,#c96a25 45%,#8c3a18)}
.ph-dumpling{background:linear-gradient(135deg,#9aa07c,#dcd6bf 50%,#7d7f66)}
.ph-skewer{background:linear-gradient(135deg,#d7b79a,#b06a4b 50%,#e7d6c4)}

/* special */
.special{height:662px;background:#fff;overflow:hidden}
.special .title{position:absolute;top:85px;width:100%}
.special .sub{position:absolute;top:122px;width:100%}
.deco-left{left:0;top:0;width:260px;height:80px;background:linear-gradient(90deg,#d9cbb0,#c49a52 60%,rgba(255,255,255,0));border-radius:0 0 60px 0}
.deco-right{right:0;top:0;width:300px;height:260px;background:linear-gradient(225deg,#5b3a2a,#a07450 45%,rgba(255,255,255,0) 75%)}
.special-item{width:360px;text-align:center;top:195px}
.special-item .plate{width:260px;height:168px;margin:0 auto;border-radius:50%}
.ph-pasta{background:radial-gradient(circle,#b05a2a 0 35%,#f0ece6 36% 62%,#fff 63%)}
.ph-cutlet{background:radial-gradient(circle,#c58a3c 0 38%,#eeeae4 39% 62%,#fff 63%)}
.special-item h4{font-family:'Oswald',sans-serif;font-weight:400;font-size:16px;color:var(--ink);margin-top:45px}
.special-item p{font-size:10px;color:var(--muted);line-height:1.5;margin:6px auto 0;width:240px}
.special-item .price{font-family:'Oswald',sans-serif;color:var(--green-light);font-size:15px;margin-top:10px}
.divider{left:586px;top:250px;width:1px;height:360px;background:var(--line)}
.dots{top:545px;width:100%;display:flex;justify-content:center;gap:8px}
.dots i{width:9px;height:9px;border-radius:50%;border:1px solid #bbb;display:block}
.dots .on{background:var(--green);border-color:var(--green)}

/* online order */
.order{height:502px;background:linear-gradient(120deg,#3a2c22,#5a4a3a 40%,#7a5a3c 65%,#4a3626)}
.order .title{position:absolute;top:70px;width:100%;color:#fff}
.order .sub{position:absolute;top:110px;width:100%;color:#fff}
.chef-figure{left:170px;top:60px;width:300px;height:442px;background:linear-gradient(180deg,#f4f4f4,#d8d8d8);border-radius:150px 150px 0 0;opacity:.9}
.field{height:30px;background:#fff;border-radius:3px;font-size:10px;color:#999;padding:0 10px;display:flex;align-items:center}
.field.area{align-items:flex-start;padding-top:8px}
.place-btn{left:514px;top:399px;width:106px;height:27px;background:var(--green);color:#fff;font-size:9px;font-weight:700;display:flex;align-items:center;justify-content:center}

/* chefs */
.chefs{height:614px;background:#fff}
.chefs .title{position:absolute;top:85px;width:100%}
.chefs .sub{position:absolute;top:120px;width:100%}
.chef-card{top:172px;width:182px;height:387px;border:1px solid var(--line);text-align:center}
.chef-card .portrait{height:244px;background:linear-gradient(180deg,#fafafa,#e4e4e4)}
.chef-card .role{font-family:'Courgette',cursive;font-size:10px;color:var(--green);margin-top:25px}
.chef-card h5{font-family:'Oswald',sans-serif;font-weight:400;font-size:15px;color:var(--ink);margin-top:8px}
.chef-card .rule{width:50px;height:1px;background:#ccc;margin:10px auto 0;position:relative}
.chef-card .rule::after{content:"";position:absolute;left:21px;top:-2px;width:8px;height:5px;background:var(--green)}
.chef-card .icons{display:flex;justify-content:center;gap:10px;margin-top:16px}
.chef-card .icons i{width:8px;height:8px;background:#bbb;display:block}

/* newsletter */
.newsletter{height:278px;background:var(--dark);text-align:center}
.newsletter p{position:absolute;top:62px;width:100%;font-size:13px;color:#bbb}
.newsletter h3{position:absolute;top:88px;width:100%;font-family:'Oswald',sans-serif;font-weight:500;font-size:27px;letter-spacing:1px;color:#fff}
.nl-input{left:245px;top:148px;width:610px;height:48px;background:#3a3a3a;color:#888;font-size:10px;display:flex;align-items:center;padding-left:20px}
.nl-btn{left:855px;top:148px;width:91px;height:48px;background:var(--green);color:#fff;font-size:10px;font-weight:700;display:flex;align-items:center;justify-content:center}

/* footer */
.site-footer{height:335px;background:var(--darker);color:#bbb}
.fcol{top:48px}
.fcol h6{font-family:'Montserrat',sans-serif;font-size:13px;color:#fff;font-weight:700;margin-bottom:18px}
.fcol p{font-size:11px;line-height:1.6;color:#bbb}
.insta{display:grid;grid-template-columns:repeat(3,52px);gap:6px}
.insta span{height:52px;background:linear-gradient(135deg,#8d9aa6,#5a6470)}
.contact li{list-style:none;font-size:11px;margin-bottom:12px;display:flex;align-items:center;gap:10px}
.contact .dot{width:8px;height:8px;border-radius:50%;background:var(--green-light)}
.fsocial{display:flex;gap:6px}
.fsocial i{width:16px;height:16px;background:var(--green);display:block}
.hours{background:#252525;width:192px;padding:12px 14px}
.hours div{display:flex;justify-content:space-between;font-size:11px;color:#fff;font-weight:600;line-height:22.6px}
.hours span{color:var(--green-light);font-weight:400}
.bottom-bar{height:42px;background:var(--green);color:#fff;font-size:11px;display:flex;align-items:center;justify-content:center}
</style>
</head>
<body>

<div class="topbar">
  <span>✉ info@dishvaultfood.com</span>
  <span>☎ +1 416 555 0142</span>
  <div class="social"><span><i></i></span><span><i></i></span><span><i></i></span><span><i></i></span></div>
</div>

<header class="site-header">
  <div class="brand abs"><b></b>Dishvault</div>
  <nav class="nav abs">
    <a class="active">HOME</a><a>ABOUT US</a><a>MENU</a><a>RESERVATION</a><a>CONTACT US</a>
  </nav>
  <div class="order-btn abs">ORDER NOW
    <svg width="16" height="10" viewBox="0 0 16 10"><path d="M1 9h14M2 8a6 6 0 0 1 12 0z" fill="#fff"/></svg>
  </div>
</header>

<section class="hero" role="img" aria-label="Restaurant table with plated salad dish and wine glass">
  <h1 class="hero-title abs">ORDER ONLINE YOUR FOOD</h1>
  <div class="hero-call abs"><em>Call Us</em> +1 416 555 0142</div>
</section>

<section class="how">
  <h2 class="title">HOW TO ORDER?</h2>
  <div class="sub">Follow These Steps</div>
  <svg class="abs" style="left:380px;top:225px" width="470" height="50" viewBox="0 0 470 50" fill="none" stroke="#bbb" stroke-width="1.5">
    <path d="M10 30 Q70 60 130 25"/><path d="M290 25 Q350 5 410 35"/>
  </svg>
  <div class="step abs" style="left:213px">
    <svg width="50" height="50" viewBox="0 0 50 50" fill="none" stroke="#333" stroke-width="2"><rect x="11" y="12" width="28" height="20" rx="2"/><path d="M6 38h38"/><circle cx="25" cy="22" r="3"/></svg>
    <div class="num">1</div><p>Choose Your<br>Location</p>
  </div>
  <div class="step abs" style="left:467px">
    <svg width="50" height="50" viewBox="0 0 50 50" fill="none" stroke="#333" stroke-width="2"><rect x="12" y="16" width="26" height="24" rx="2"/><path d="M18 16v-4a7 7 0 0 1 14 0v4M12 26h26"/></svg>
    <div class="num">2</div><p>Make your<br>order</p>
  </div>
  <div class="step abs" style="left:761px">
    <svg width="60" height="50" viewBox="0 0 60 50" fill="none" stroke="#333" stroke-width="2"><circle cx="15" cy="38" r="6"/><circle cx="45" cy="38" r="6"/><path d="M15 38h30M22 38l6-14h10l7 14M30 12h10v12H30z"/></svg>
    <div class="num">3</div><p>Delivery or<br>take out</p>
  </div>
</section>

<section class="menu">
  <h2 class="title">DISHVAULT MENU</h2>
  <div class="sub">Follow These Steps</div>
  <div class="tabs abs"><span class="on">APPETIZER</span><span>DESERTS</span><span>DRINK</span><span>LUNCH</span><span>MAIN</span></div>

  <div class="dish-card abs" style="left:206px;top:251px"><div class="photo ph-toast" role="img" aria-label="French toast with strawberries and blueberries"></div><div class="price">Only $7</div><div class="name">2-pc Pork BBQ ( 1 Side)</div></div>
  <div class="dish-card abs" style="left:475px;top:251px"><div class="photo ph-chicken" role="img" aria-label="Roast chicken leg with salad"></div><div class="price">Only $20</div><div class="name">Pring Veg &amp; Pasta</div></div>
  <div class="dish-card abs" style="left:744px;top:251px"><div class="photo ph-dumpling" role="img" aria-label="Steamed dumplings with dipping sauce"></div><div class="price">Only $19</div><div class="name">Very Bacon</div></div>
  <div class="dish-card abs" style="left:206px;top:581px"><div class="photo ph-toast" role="img" aria-label="French toast with strawberries and blueberries"></div><div class="price">Only $7</div><div class="name">2-pc Pork BBQ ( 1 Side)</div></div>
  <div class="dish-card abs" style="left:475px;top:581px"><div class="photo ph-skewer" role="img" aria-label="Grilled skewers on a plate"></div><div class="price">Only $18</div><div class="name">Plenty a Pepperoni</div></div>
  <div class="dish-card abs" style="left:744px;top:581px"><div class="photo ph-chicken" role="img" aria-label="Roast chicken leg with salad"></div><div class="price">Only $20</div><div class="name">Pring Veg &amp; Pasta</div></div>
</section>

<section class="special">
  <div class="deco-left abs" role="img" aria-label="Bread and a cup of honey tea on the table"></div>
  <div class="deco-right abs" role="img" aria-label="Wooden tray with small bowls of food"></div>
  <h2 class="title">TODAY SPECIAL DISH</h2>
  <div class="sub">Delas Today</div>
  <div class="special-item abs" style="left:207px">
    <div class="plate ph-pasta" role="img" aria-label="Plate of noodles with chopsticks"></div>
    <h4>Pring Veg &amp; Pasta</h4>
    <p>Fresh pasta tossed with seasonal greens and light herb sauce, served warm daily.</p>
    <div class="price">Only $15</div>
  </div>
  <div class="divider abs"></div>
  <div class="special-item abs" style="left:594px">
    <div class="plate ph-cutlet" role="img" aria-label="Grilled cutlet with greens and cutlery"></div>
    <h4>Pring Veg &amp; Pasta</h4>
    <p>Grilled lean cutlet with crisp salad leaves and lemon, prepared fresh each day.</p>
    <div class="price">Only $30</div>
  </div>
  <div class="dots abs"><i class="on"></i><i></i><i></i><i></i></div>
</section>

<section class="order" role="img" aria-label="Dark background of a cooked meal">
  <div class="chef-figure abs" role="img" aria-label="Chef in white uniform holding a tablet"></div>
  <h2 class="title">ONLINE ORDER</h2>
  <div class="sub">Book Now</div>
  <div class="field abs" style="left:514px;top:200px;width:239px">Name</div>
  <div class="field abs" style="left:774px;top:200px;width:239px">Email Address</div>
  <div class="field abs" style="left:514px;top:245px;width:239px">Phone No.</div>
  <div class="field abs" style="left:774px;top:245px;width:239px">Select Chef</div>
  <div class="field area abs" style="left:514px;top:290px;width:499px;height:91px">Order Details</div>
  <div class="place-btn abs">PLACE ORDER</div>
</section>

<section class="chefs">
  <h2 class="title">BEST CHEFS FOR YOU</h2>
  <div class="sub">Chef Team</div>
  <div class="chef-card abs" style="left:212px"><div class="portrait" role="img" aria-label="Chef in white uniform and hat"></div><div class="role">Senior Chef</div><h5>Carlo Maren</h5><div class="rule"></div><div class="icons"><i></i><i></i><i></i></div></div>
  <div class="chef-card abs" style="left:411px"><div class="portrait" role="img" aria-label="Chef in white uniform and hat"></div><div class="role">Junior Chef</div><h5>Carlo Maren</h5><div class="rule"></div><div class="icons"><i></i><i></i><i></i></div></div>
  <div class="chef-card abs" style="left:614px"><div class="portrait" role="img" aria-label="Chef holding a wooden spoon"></div><div class="role">Sous Chef</div><h5>Carlo Maren</h5><div class="rule"></div><div class="icons"><i></i><i></i><i></i></div></div>
  <div class="chef-card abs" style="left:813px"><div class="portrait" role="img" aria-label="Chef holding a tomato"></div><div class="role">Pastry Chef</div><h5>Carlo Maren</h5><div class="rule"></div><div class="icons"><i></i><i></i><i></i></div></div>
</section>

<section class="newsletter">
  <p>Subscribe to our newsletter and never miss a special offer</p>
  <h3>MY BEARDED NEWSLETTER</h3>
  <div class="nl-input abs">ENTER YOUR EMAIL ADDRESS</div>
  <div class="nl-btn abs">SUBSCRIBE</div>
</section>

<footer class="site-footer">
  <div class="fcol abs" style="left:160px;width:200px">
    <h6>ABOUT US</h6>
    <p>Fresh meals prepared daily for athletes and active people across the city. Balanced portions, clean ingredients, delivered to your door or ready for pickup.</p>
  </div>
  <div class="fcol abs" style="left:396px">
    <h6>OUR INSTAGRAM</h6>
    <div class="insta" role="img" aria-label="Grid of six meal photos"><span></span><span></span><span></span><span></span><span></span><span></span></div>
  </div>
  <div class="fcol abs" style="left:617px">
    <h6>CONTACT US</h6>
    <ul class="contact">
      <li><i class="dot"></i>+1 416 555 0142</li>
      <li><i class="dot"></i>info@dishvaultfood.com</li>
      <li><i class="dot"></i>www.dishvaultfood.com</li>
    </ul>
    <div class="fsocial"><i></i><i></i><i></i><i></i></div>
  </div>
  <div class="fcol abs" style="left:846px">
    <h6>OPENING HOURS</h6>
    <div class="hours">
      <div>Monday<span>08:00 - 20:00</span></div>
      <div>Tuesday<span>08:00 - 20:00</span></div>
      <div>Wednesday<span>08:00 - 20:00</span></div>
      <div>Thursday<span>08:00 - 20:00</span></div>
      <div>Friday<span>08:00 - 20:00</span></div>
      <div>Saturday<span>08:00 - 20:00</span></div>
      <div>Sunday<span>08:00 - 20:00</span></div>
    </div>
  </div>
</footer>
<div class="bottom-bar">Copyright © 2017 Dishvault</div>

</body>
</html>
```